Fahrzeugbeschriftung für Industriemaler-Unternehmen
Tolle Designer und sehr geduldig.
Zielgruppe
Wir sind Industriemaler Unternehmen und suchen ein hochwertiges und elegantes Design, unsere Zielgruppen sind allgemein in der Industrie Branche tätig, wie z. B. Medizinischer- und Technischer Gerätebau. Dazu gehören technische Kunststoffteile, Präzisionteile, Kleinmaschinen, Messgeräte, usw.
Aufgabenstellung
Das Design sollte präzis, elegant und Modern sein. Farbenkombination sollte mit Schwarzer Hintergrund sein, da unsere Fahrzeuge Schwarz sind. Wir sind in einem 2 sprachigen Standort tätig, daher sollte der design Deutsch und Französisch sein. Damit Sie einen besseren Überblick haben, können Sie gerne unsere Webseite anschauen. Als Bildmaterial haben wir nur unseren Logo.
Horizon Laque Atelier Sàrl
Birkenweg 14b
2563 Ipsach
info@laqueatelier-exemple.ch
www.laqueatelier-exemple.ch

```html
<!DOCTYPE html>
<html lang="de">
<head>
<meta charset="utf-8">
<title>Horizon Laque Atelier – Fahrzeugbeschriftung</title>
<link rel="stylesheet" href="https://fonts.googleapis.com/css2?family=Montserrat:ital,wght@0,500;0,600;1,600&display=swap">
<style>
  :root {
    --backdrop: #e6e8ec;
    --wrap-black: #0b0b0c;
    --panel-edge: #1c1c1e;
    --text-white: #ffffff;
    --splash-orange: #f26a1b;
    --splash-yellow: #f5d21a;
    --splash-green: #4cc23a;
    --splash-blue: #2a7de1;
    --splash-magenta: #d8248f;
    --splash-red: #e8343a;
  }
  * { margin: 0; padding: 0; box-sizing: border-box; }
  html, body {
    width: 1200px;
    height: 800px;
    overflow: hidden;
    background: var(--backdrop);
    font-family: "Montserrat", Arial, sans-serif;
  }
  .vehicle-side {
    position: absolute;
    left: 60px;
    top: 150px;
    width: 1080px;
    height: 500px;
    background: var(--wrap-black);
    border: 2px solid var(--panel-edge);
    border-radius: 28px;
    overflow: hidden;
  }
  .splash { position: absolute; }
  .splash--front { left: 40px; top: 150px; width: 290px; height: 340px; }
  .splash--rear { left: 975px; top: 240px; width: 100px; height: 250px; }
  .mascot-illustration {
    position: absolute;
    left: 840px;
    top: 24px;
    width: 200px;
    height: 180px;
    border-radius: 50%;
    background: radial-gradient(circle at 35% 40%, var(--splash-green) 0%, var(--splash-yellow) 30%, var(--splash-blue) 60%, var(--splash-magenta) 85%, var(--splash-orange) 100%);
    opacity: 0.9;
  }
  .brand-name {
    position: absolute;
    left: 560px;
    top: 250px;
    color: var(--text-white);
    font-weight: 500;
    font-size: 44px;
    letter-spacing: -0.5px;
    line-height: 1;
  }
  .company-address {
    position: absolute;
    left: 300px;
    top: 256px;
    width: 230px;
    text-align: right;
    color: var(--text-white);
    font-style: normal;
    font-weight: 600;
    font-size: 13px;
    line-height: 1.45;
  }
  .contact-line {
    position: absolute;
    top: 418px;
    color: var(--text-white);
    font-weight: 600;
    font-style: italic;
    font-size: 18px;
  }
  .contact-line--web { left: 360px; }
  .contact-line--mail { left: 670px; }
</style>
</head>
<body>
  <main class="vehicle-side">
    <svg class="splash splash--front" viewBox="0 0 300 340" preserveAspectRatio="none" role="img" aria-label="Farbspritzer in Regenbogenfarben um den vorderen Radlauf">
      <defs>
        <linearGradient id="front-splash-tone" x1="0" y1="0" x2="1" y2="1">
          <stop offset="0" stop-color="var(--splash-red)"/>
          <stop offset="0.3" stop-color="var(--splash-orange)"/>
          <stop offset="0.55" stop-color="var(--splash-yellow)"/>
          <stop offset="0.75" stop-color="var(--splash-blue)"/>
          <stop offset="1" stop-color="var(--splash-magenta)"/>
        </linearGradient>
      </defs>
      <path d="M150 20 C230 30 290 110 280 200 C270 280 220 330 170 320 C200 250 170 180 110 170 C60 165 20 200 10 240 C0 160 60 30 150 20 Z" fill="url(#front-splash-tone)" opacity="0.85"/>
    </svg>

    <svg class="splash splash--rear" viewBox="0 0 100 250" preserveAspectRatio="none" role="img" aria-label="Farbspritzer in Regenbogenfarben um den hinteren Radlauf">
      <defs>
        <linearGradient id="rear-splash-tone" x1="0" y1="0" x2="1" y2="1">
          <stop offset="0" stop-color="var(--splash-blue)"/>
          <stop offset="0.35" stop-color="var(--splash-green)"/>
          <stop offset="0.65" stop-color="var(--splash-magenta)"/>
          <stop offset="1" stop-color="var(--splash-orange)"/>
        </linearGradient>
      </defs>
      <path d="M60 10 C90 30 100 90 100 150 L100 250 C90 190 60 150 30 160 C10 170 5 200 0 230 C0 140 20 30 60 10 Z" fill="url(#rear-splash-tone)" opacity="0.85"/>
    </svg>

    <div class="mascot-illustration" role="img" aria-label="Farbenfrohe Maskottchen-Illustration in Regenbogentönen"></div>

    <div class="brand-name">Horizon Laque</div>

    <address class="company-address">
      Horizon Laque Atelier Sàrl<br>
      Birkenweg 14b<br>
      2563 Ipsach
    </address>

    <p class="contact-line contact-line--web">www.laqueatelier-exemple.ch</p>
    <p class="contact-line contact-line--mail">info@laqueatelier-exemple.ch</p>
  </main>
</body>
</html>
```